Coded Website Design

I am opening a sustainable home consulting business. The core service areas will be lawn maintenance, sustainable landscape maintenance, Composting, Vermiculture, and Rain Harvesting. We will be designing sustainability programs metrics for the home owners and their families to demonstrate cost savings and the environmental impact of their efforts. We will use clean fueled equipment with a heavy emphasis electric powered equipment energized by solar powered chargers.

The purpose of the site:
Provide information on the company and services to potential customers.
Allow for customers to log in and schedule services, ask questions, pay bills and buy products.
Have a green living section with tips and resource's.
I will have a Chatterbox Page, Pipster, account Nuvola Ring, and a Quillstack blog set up in the company name. I would like the web presents and social
media have the same theme, common vocabulary and navigation.

The address for the site will be: bramwickyardco.example
Updates

Hi Everyone. The project has been temporarily closed since the client will be posting a logo design project. It will be reopened after the client has acquired a logo design, to be provided for this project.

Thanks,
QB Admin

Reason: I would like to give the designers additional time to submit proposals and allow myself adequate time to review and work with designers. While I am anxious to get the website design done and up for use, I do not want either the designers nor myself to feel that this is being rushed and unnecessarily compromise the design process due to a date constraint. I would like to get the best design and website I can and find the right designer to work with to accomplish this goal.

Thank you for those who have submitted a design.  I apologize for not having provided feedback to you, I was injured in an accident and have been unable to attend to work while I was recuperating.  I am going to extend the design period for an additional 7 days after which I will be back to work fulltime and work towards making a final selection.  I will be sending feedback to the designs previously submitted over the next few days.  Thank you again to the designers who have submitted designs, your patients and understanding.  

Reason: Thank you for those who have submitted a design. I apologize for not having provided feedback to you, I was injured in an accident and have been unable to attend to work while I was recuperating. I am going to extend the design period for an additional 7 days after which I will be back to work fulltime and work towards making a final selection. I will be sending feedback to the designs previously submitted over the next few days. Thank you again to the designers who have submitted designs, your patients and understanding.

Target Market(s)

Charlotte North Carolina Familys with an intgerest in sustainability and green living

Industry/Entity Type

Sustainability

Requirements
Must have
• I like techno sites that are not imposing and or intimidating, and that utilize technology in a way that makes the experience memorable.

I like sites that are easy and intuitive to navigate.

I like the home page to tell a story using sound, voice, graphics, pictures to guide the customer to the next page. I don't like looking at a borage of text blocks .

it needs to be able to schedule appointments and services, purchase merchandise, pay bills, offer feedback

the blog, website and if possible app should be an extension of each other and be easy to go from one to the other
Nice to have
• easy navigation, be fun, teach something new, tell a story, be memorable

I like pages that utilize flash.
I really like http://plumtreeworks.example/examples.php
Should not have
• I don't like sites that are a series of text blocks that look like the yellow pages.

I don't like navigation that is circular in nature

redundancy is not good unless necessary

```html
<!DOCTYPE html>
<html lang="en">
<head>
<meta charset="utf-8">
<title>Bramwick Yard Co</title>
<link rel="stylesheet" href="https://fonts.googleapis.com/css2?family=Cinzel:wght@400;700&family=Open+Sans:wght@400;600&display=swap">
<style>
:root{
  --night:#03161c;
  --ink:#000;
  --white:#fff;
  --leaf:#8cc63f;
  --sky:#0aa3d8;
  --sky-dark:#0788c0;
  --panel:#efefef;
  --foot:#e1e1e1;
  --foot-text:#333;
  --muted:#8a9499;
}
*{box-sizing:border-box;margin:0;padding:0}
html,body{width:949px;height:1200px;overflow:hidden}
body{background:var(--night);font-family:"Cinzel",serif;color:var(--white);position:relative}
.abs{position:absolute}

/* header */
.brand{left:17px;top:18px;width:160px}
.brand-mark{width:84px;height:52px;margin-left:38px;display:block}
.brand-name{font-size:17px;color:var(--muted);letter-spacing:1px;margin-top:10px;white-space:nowrap}
.login{left:818px;top:23px;width:112px;height:23px;border-radius:4px;background:linear-gradient(#9ed64e,#6fab22);
  font-family:"Open Sans",sans-serif;font-size:12px;font-weight:600;text-align:center;line-height:23px}
.nav{left:245px;top:60px;height:50px;display:flex;align-items:center;font-size:15px;font-weight:700;letter-spacing:.5px}
.nav a{color:var(--white);text-decoration:none;position:relative}
.nav .sep{display:inline-block;width:1px;height:24px;background:var(--leaf);transform:skewX(-35deg);margin:0 20px}
.nav .active{color:var(--sky);padding:14px 18px}
.nav .active svg{position:absolute;left:0;top:0;width:84px;height:48px}

/* hero */
.hero{left:17px;top:128px;width:911px;height:296px;background:linear-gradient(120deg,#3f5c2a 0%,#5b7b3a 35%,#3a5d8f 55%,#8aa65c 80%,#a9c67a 100%)}
.hero-band{left:17px;top:424px;width:911px;height:65px;background:var(--ink);font-size:17px;font-weight:700;letter-spacing:.3px}
.hero-band li{list-style:none;position:absolute;padding-left:22px;white-space:nowrap}
.hero-band li::before{content:"";position:absolute;left:4px;top:6px;border-left:6px solid var(--sky);border-top:4px solid transparent;border-bottom:4px solid transparent}

/* welcome */
.welcome{left:20px;top:504px;width:580px}
.welcome h1{font-size:18px;font-weight:400;color:var(--sky);margin-bottom:12px}
.welcome p{font-size:11.5px;line-height:17px;text-align:justify;margin-bottom:10px}
.more{left:537px;top:688px;font-size:11.5px;color:var(--sky)}

.ask{left:625px;top:509px;width:305px;height:191px;background:var(--panel);color:#222}
.ask h2{height:34px;background:var(--sky);color:var(--white);font-size:12.5px;font-weight:700;line-height:34px;padding-left:9px}
.field{position:absolute;left:0;width:100%;font-size:12px}
.field label{position:absolute;right:215px;top:6px;white-space:nowrap}
.field span{position:absolute;left:89px;width:199px;height:26px;background:linear-gradient(#e2e2e2,#fafafa);border:1px solid #bbb;border-radius:2px}
.signup{position:absolute;left:220px;top:143px;width:66px;height:27px;background:linear-gradient(var(--sky),var(--sky-dark));border-radius:3px;color:var(--white);font-size:12px;text-align:center;line-height:27px}

/* services */
.services-title{left:0;top:712px;width:949px;text-align:center;font-size:19px;color:var(--sky)}
.arrow{top:822px}
.service{top:750px;width:175px;height:175px}
.service .disc{width:175px;height:175px;border-radius:50%;border:6px solid #e8e8e8;overflow:hidden}
.service.current .disc{border-color:var(--sky)}
.service .tag{position:absolute;left:0;top:145px;width:175px;height:30px;background:var(--sky);text-align:center;line-height:30px;font-size:13.5px;white-space:nowrap}
.service.current .tag{background:var(--leaf);color:#1b2a0a;top:142px}
.service .tag.small{font-size:11px}

/* footer */
.footer{left:0;top:946px;width:949px;height:176px;background:var(--foot);color:var(--foot-text)}
.col{position:absolute;top:18px;font-size:11.5px;line-height:19px}
.col h3{font-size:11.5px;font-weight:700;margin-bottom:4px;color:#111}
.col-shade{position:absolute;top:18px;width:22px;height:124px;background:linear-gradient(90deg,rgba(0,0,0,.12),rgba(0,0,0,0))}
.social li{list-style:none;display:flex;align-items:center;height:30px}
.social i{display:inline-block;width:22px;height:22px;margin-right:8px;border-radius:3px}
.map{left:775px;top:20px;width:128px;height:82px;background:linear-gradient(135deg,#dfe4d6,#cfd8c6 60%,#e6e2d8)}
.legal{left:0;top:1140px;width:949px;text-align:center;font-family:"Open Sans",sans-serif;font-size:12px}
</style>
</head>
<body>

<header>
  <div class="abs brand">
    <svg class="brand-mark" viewBox="0 0 84 52" aria-hidden="true"><rect x="18" y="6" width="40" height="40" rx="4" fill="#8cc63f"/></svg>
    <div class="brand-name">BRAMWICK YARD CO</div>
  </div>
  <div class="abs login">Login / Register</div>
  <nav class="abs nav">
    <a class="active" href="#"><svg viewBox="0 0 84 48" aria-hidden="true"><path d="M4 8 Q40 -2 72 14 Q84 30 82 46 Q50 50 20 44" fill="none" stroke="#8cc63f" stroke-width="3"/><path d="M6 10 Q8 34 30 44 Q58 50 82 46" fill="none" stroke="#0aa3d8" stroke-width="3"/></svg>Home</a>
    <span class="sep"></span><a href="#">About Us</a>
    <span class="sep"></span><a href="#">Service</a>
    <span class="sep"></span><a href="#">Products</a>
    <span class="sep"></span><a href="#">Our work</a>
    <span class="sep"></span><a href="#">Contact Us</a>
  </nav>
</header>

<div class="abs hero" role="img" aria-label="Photo of two gardeners kneeling beside a hedge on a grassy lawn"></div>
<ul class="abs hero-band">
  <li style="left:18px;top:10px">Lawn Maintenance</li>
  <li style="left:18px;top:38px">Sustainable Landscape Maintenance</li>
  <li style="left:510px;top:10px">Composting</li>
  <li style="left:510px;top:38px">Vermiculture</li>
  <li style="left:760px;top:22px;padding-left:12px">Rain Harvesting</li>
</ul>

<section class="abs welcome">
  <h1>Welcome to bramwickyardco.example</h1>
  <p>Lorem ipsum dolor sit amet, consectetur adipiscing elit. Phasellus blandit massa eu neque aliquet laoreet. Nullam tempor velit ac elit blandit eget faucibus augue hendrerit. Mauris a dignissim ipsum. Proin mi velit, vehicula et ultrices egestas, porta vel dui. Donec facilisis libero</p>
  <p>Pulvinar lorem convallis ultrices bibendum elit rutrum. Morbi imperdiet dapibus nibh, condimentum euismod odio congue a.Sed blandit semper lacinia. Nunc ut urna ac dui suscipit suscipit vel ut lectus. Maecenas consectetur feugiat felis viverra facilisisLorem ipsum dolor sit amet, consectetur adipiscing elit.</p>
</section>
<div class="abs more">Read More</div>

<aside class="abs ask">
  <h2>Ask a Question</h2>
  <div class="field" style="top:53px"><label>First Name</label><span></span></div>
  <div class="field" style="top:99px"><label>Email</label><span></span></div>
  <div class="signup">Sign Up</div>
</aside>

<h2 class="abs services-title" style="font-weight:400">Our Services</h2>
<svg class="abs arrow" style="left:0" width="16" height="28" viewBox="0 0 16 28" aria-hidden="true"><path d="M14 2 L3 14 L14 26" fill="none" stroke="#0aa3d8" stroke-width="3"/></svg>
<svg class="abs arrow" style="left:933px" width="16" height="28" viewBox="0 0 16 28" aria-hidden="true"><path d="M2 2 L13 14 L2 26" fill="none" stroke="#0aa3d8" stroke-width="3"/></svg>

<div class="abs service current" style="left:20px"><div class="disc" role="img" aria-label="Photo of a push reel mower on grass" style="background:linear-gradient(#3c4a30,#7fae3c)"></div><div class="tag">Lawn Maintenance</div></div>
<div class="abs service" style="left:203px"><div class="disc" role="img" aria-label="Photo of a group planting flowers in a garden" style="background:linear-gradient(#5b7a3a,#9fb86a)"></div><div class="tag small">Landscape Maintenance</div></div>
<div class="abs service" style="left:387px"><div class="disc" role="img" aria-label="Photo of boots and a garden fork in soil" style="background:linear-gradient(#6f7a5c,#4a3a2a)"></div><div class="tag">Composting</div></div>
<div class="abs service" style="left:571px"><div class="disc" role="img" aria-label="Photo of worms in dark soil" style="background:linear-gradient(#3a2a1e,#5a4030)"></div><div class="tag">Vermiculture</div></div>
<div class="abs service" style="left:755px"><div class="disc" role="img" aria-label="Photo of a rain barrel beneath a downpipe" style="background:linear-gradient(#8a9a6a,#c8c8c4)"></div><div class="tag">Rain Harvesting</div></div>

<footer class="abs footer">
  <div class="col" style="left:19px"><h3>Main Links</h3>Home<br>About Us<br>Products<br>Our work<br>Contact Us</div>
  <div class="col-shade" style="left:135px"></div>
  <div class="col" style="left:208px"><h3>Other Links</h3>About Us<br>Products<br>Our work<br>Contact Us</div>
  <div class="col-shade" style="left:315px"></div>
  <div class="col" style="left:361px"><h3 style="padding-left:28px">Follow Us</h3>
    <ul class="social">
      <li><i style="background:#3b5b98"></i>Chatterbox</li>
      <li><i style="background:#5bc0de"></i>Pipster</li>
      <li><i style="background:#1f74b0"></i>Linkwise</li>
      <li><i style="background:#3b9a46;border-radius:50%"></i>Nuvola Ring</li>
    </ul>
  </div>
  <div class="col-shade" style="left:484px"></div>
  <div class="col" style="left:538px"><h3>Contact</h3>Toll free (555) 014-2290<br>Phone:(555) 014-2291<br>Fax: (555) 014-2292<br>Email: info@bramwickyardco.example</div>
  <div class="abs map" role="img" aria-label="Small location map"></div>
</footer>

<p class="abs legal">Copyright@2013 bramwickyardco.example. All Rights Reserved</p>
</body>
</html>
```